Manuka honey wholesales and exports

We need business cards for our honey distribution company based in New Zealand. We supply shops locally and export Manuka honey around the world.
We deal with a very high quality and 100% natural product that can be used for medical, general health as well as food. We are looking business cards that show our honey products are of a high quality with a modern look.

Target Market(s)

Health and medical retailers and importers

Industry/Entity Type

Wholesale

Contact Information for Business Card

Tevin Apiary NZ Limited

www.tevinapiarynz.example

Derek Fawley

M +64 219036482

E tevinapiarynz@mailbox.example

PO Box 58-214
Takapuna
North Shore
Auckland
New Zealand

Font styles to use
Serif

Requirements
Must have
• (Tevin Apiary NZ Limited) with some artwork on one side and all details on the other side.
Nice to have
• I have seen a very simple card with large yellow and black stripes on one side with a company name.. looked clean and simple so something similar or just let the creative beast inside you take over and we will see what you can come up with.

```html
<!DOCTYPE html>
<html lang="en">
<head>
<meta charset="utf-8">
<title>Tevin Apiary NZ Limited — Business Card</title>
<link rel="stylesheet" href="https://fonts.googleapis.com/css2?family=Ubuntu:wght@400;500;700&display=swap">
<style>
  :root {
    --page: #d9d9d9;
    --card: #252525;
    --card-edge: #2c2c2c;
    --red: #d81e1e;
    --line-red: #a81a1a;
    --white: #f2f2f2;
    --muted: #e4e4e4;
  }
  * { box-sizing: border-box; margin: 0; padding: 0; }
  html, body {
    width: 1200px; height: 1200px; overflow: hidden;
    background: var(--page);
    font-family: "Ubuntu", sans-serif;
  }
  .canvas { position: relative; width: 1200px; height: 1200px; }
  .card {
    position: absolute; left: 150px; width: 900px; height: 514px;
    background: linear-gradient(135deg, var(--card-edge), var(--card));
    overflow: hidden;
    box-shadow: 0 6px 18px rgba(0,0,0,.18);
  }
  .card--front { top: 60px; }
  .card--back { top: 620px; }
  .rules { position: absolute; left: 0; top: 0; width: 900px; height: 514px; }

  /* front */
  .brand-name {
    position: absolute; left: 40px; top: 200px;
    font-weight: 700; font-size: 40px; letter-spacing: .5px;
    text-transform: uppercase; color: var(--white);
  }
  .brand-band { position: absolute; left: 0; top: 252px; width: 580px; height: 48px; }
  .brand-web {
    position: absolute; left: 150px; top: 258px;
    font-size: 24px; color: var(--white); letter-spacing: .5px;
  }

  /* back */
  .person-name {
    position: absolute; left: 170px; top: 300px;
    font-size: 36px; color: var(--white);
  }
  .person-band {
    position: absolute; left: 0; top: 350px; width: 420px; height: 42px;
    background: var(--red);
  }
  .person-role {
    position: absolute; left: 240px; top: 355px;
    font-size: 26px; font-weight: 500; color: var(--white);
  }
  .contact-list { position: absolute; left: 480px; top: 128px; list-style: none; width: 390px; }
  .contact-item {
    display: flex; align-items: center; gap: 14px;
    height: 52px; border-bottom: 1px solid var(--line-red);
    font-size: 21px; color: var(--muted);
  }
  .contact-item--address { height: auto; padding: 8px 0 10px; align-items: flex-start; }
  .contact-badge {
    flex: none; width: 32px; height: 32px; border-radius: 50%;
    background: var(--red); color: var(--white);
    display: flex; align-items: center; justify-content: center;
    font-size: 17px;
  }
  .contact-address { line-height: 1.55; }
</style>
</head>
<body>
<div class="canvas">

  <section class="card card--front" aria-label="Card front">
    <svg class="rules" viewBox="0 0 900 514" aria-hidden="true">
      <g stroke="#b01c1c" stroke-width="1.2">
        <line x1="0" y1="44" x2="900" y2="44"/><line x1="0" y1="50" x2="900" y2="50"/>
        <line x1="0" y1="56" x2="900" y2="56"/><line x1="0" y1="62" x2="900" y2="62"/>
        <line x1="0" y1="436" x2="900" y2="436"/><line x1="0" y1="442" x2="900" y2="442"/>
        <line x1="0" y1="448" x2="900" y2="448"/><line x1="0" y1="454" x2="900" y2="454"/>
      </g>
    </svg>
    <svg class="brand-band" viewBox="0 0 580 48" aria-hidden="true">
      <polygon points="0,0 562,0 580,24 562,48 0,48" fill="var(--red)"/>
    </svg>
    <h1 class="brand-name">Tevin Apiary NZ Limited</h1>
    <p class="brand-web">www.tevinapiarynz.example</p>
  </section>

  <section class="card card--back" aria-label="Card back">
    <svg class="rules" viewBox="0 0 900 514" aria-hidden="true">
      <g stroke="#b01c1c" stroke-width="1.2">
        <line x1="0" y1="44" x2="900" y2="44"/><line x1="0" y1="50" x2="900" y2="50"/>
        <line x1="0" y1="56" x2="900" y2="56"/><line x1="0" y1="62" x2="900" y2="62"/>
        <line x1="0" y1="452" x2="900" y2="452"/><line x1="0" y1="458" x2="900" y2="458"/>
        <line x1="0" y1="464" x2="900" y2="464"/><line x1="0" y1="470" x2="900" y2="470"/>
      </g>
    </svg>
    <h2 class="person-name">Derek Fawley</h2>
    <div class="person-band"></div>
    <p class="person-role">Designer</p>

    <ul class="contact-list">
      <li class="contact-item"><span class="contact-badge">P</span>+64 219036482</li>
      <li class="contact-item"><span class="contact-badge">M</span>tevinapiarynz@mailbox.example</li>
      <li class="contact-item"><span class="contact-badge">W</span>www.tevinapiarynz.example</li>
      <li class="contact-item contact-item--address"><span class="contact-badge">A</span>
        <span class="contact-address">PO Box 58-214, Takapuna North<br>Shore, Auckland, New Zealand</span></li>
    </ul>
  </section>

</div>
</body>
</html>
```